Maine Organic farm needs a label design for various food products

We need a label design that we can use across a variety of vegetable-based food products that we produce using some of our organic vegetables that we grow on our farm located in Maine, USA.
Our products include:
1) a Traditional and Vegan Korean Kimchi
2) Pomrak Sauce (a Korean Hot Sauce)
3) Pickles of Brambleton Relish
4) Radishtastic Chutney
5) Seasonal Soups (many varieties, depending on what's available during the season)
6) Iron Oath Maple Syrup (we are retired from the U.S. Harbor Guard, hence the name and spelling)
7) Maine Wild Blueberry Kombucha (made with organic Maine wild blueberries)

For the Korean products (kimchi and Pomrak Sauce) we would like to incorporate the Korean chili pepper (red) and chopsticks. The attached picture was taken from the internet, it has not been trademarked, but I am hesitant to use it as is as our business expands. Would like the "kimchi" to somehow incorporate the chopstick and pepper, but not look exactly like the attached image.

The final design should communicate farm fresh, organic, healthy and high quality ingredients, and Maine-made. All of our products go into glass jars 16oz and 8 oz. The hot sauce goes into 5.5oz and 8 oz bottles, the Maple Syrup goes into 8oz and 16oz bottles, and a 12oz bottle for the Kombucha. We will need the flexibility of changing some components of the label to accommodate each different food product.

The labels do not have the encircle the entirety of the jar. We understand that this is a tall order to fit so many different products. We are hoping that once we get the feel and design down, we can work with you for a fee outside of the competition to finalize other products labels on different sizes jars, bottles, etc. Its most important that we get the right feel for a label that can be used for a wide variety of food products.

Target Market(s)

Health conscious, foodies, local farm supporters

Font styles to use
Serif
Decorative
Script

Colors

Designer to choose colors to be used in the design.

Requirements
Must have
• Fenwick Hollow Farm Logo. Room for product name (interchangeable per product), ingredients list, space for jar size (8 oz, 12 oz, 16 oz). On Korean products -must have Korean hot chili pepper and chopsticks
Nice to have
• We'd like something fairly bold and rustic looking.
Should not have
• Nothing too modern or industrial looking. Nothing hippy-ish. Clean and professional. No cartoonish looking letters or designs.

```html
<!DOCTYPE html>
<html lang="en">
<head>
<meta charset="utf-8">
<title>Fenwick Hollow Farm Labels</title>
<link href="https://fonts.googleapis.com/css2?family=Oswald:wght@700&family=Arvo:ital,wght@0,700;1,700&family=Noto+Serif:ital@0,400;1,400&display=swap" rel="stylesheet">
<style>
  :root {
    --bg: #f2f2f2;
    --label: #ffffff;
    --ink: #1a1a1a;
    --navy: #1f3652;
    --sketch-a: #efe9e0;
    --sketch-b: #ffffff;
    --chili: #c8281e;
    --stick: #7a4a2a;
    --muted: #444444;
  }
  * { box-sizing: border-box; margin: 0; padding: 0; }
  html, body { width: 1053px; height: 1200px; overflow: hidden; }
  body { background: var(--bg); position: relative; font-family: "Noto Serif", serif; color: var(--ink); }

  .label {
    position: absolute;
    background: var(--label);
    box-shadow: 0 2px 10px rgba(0,0,0,0.08);
    overflow: hidden;
  }
  .label > * { position: absolute; line-height: 1; }
  .label--syrup { left: 144px; top: 580px; width: 382px; height: 338px; }
  .label--sauce { left: 627px; top: 602px; width: 219px; height: 302px; }

  .farm-scene {
    left: 0; top: 0; width: 100%;
    background: linear-gradient(180deg, var(--sketch-a) 0%, var(--sketch-b) 100%);
  }
  .label--syrup .farm-scene { height: 100px; }
  .label--sauce .farm-scene { height: 90px; }

  .brand {
    display: flex; align-items: center; justify-content: center; gap: 5px;
    font-family: "Arvo", serif; font-weight: 700; color: var(--navy); white-space: nowrap;
  }
  .brand__dot { border-radius: 50%; background: var(--navy); flex: none; }

  .center-line { left: 0; width: 100%; text-align: center; white-space: nowrap; }

  .product-name { font-family: "Oswald", sans-serif; font-weight: 700; letter-spacing: 0.5px; }
  .product-type { font-family: "Arvo", serif; font-weight: 700; }
  .ingredients { font-family: "Arvo", serif; font-style: italic; font-weight: 700; text-align: center; line-height: 1.3; }
  .meta-row { display: flex; justify-content: space-between; align-items: baseline; }
  .meta-row__note { font-style: italic; color: var(--muted); }
  .address { font-family: "Arvo", serif; font-weight: 700; }

  /* syrup */
  .label--syrup .brand { left: 0; width: 100%; top: 56px; font-size: 16px; }
  .label--syrup .brand__dot { width: 11px; height: 11px; }
  .label--syrup .product-name { top: 130px; font-size: 54px; }
  .label--syrup .product-type { top: 191px; font-size: 22px; }
  .label--syrup .ingredients { left: 30px; right: 30px; top: 250px; font-size: 10.5px; }
  .label--syrup .meta-row { left: 34px; right: 34px; top: 290px; }
  .label--syrup .meta-row__note { font-size: 8px; }
  .label--syrup .meta-row__size { font-size: 13px; }
  .label--syrup .address { top: 315px; font-size: 11px; }

  /* sauce */
  .label--sauce .brand { left: 12px; width: 146px; top: 50px; font-size: 9px; gap: 4px; }
  .label--sauce .brand__dot { width: 7px; height: 7px; }
  .korean-art {
    left: 164px; top: 46px; width: 42px; height: 100px;
    background: linear-gradient(160deg, var(--stick) 0%, var(--stick) 55%, var(--chili) 100%);
    opacity: 0.85; border-radius: 4px;
  }
  .label--sauce .product-name { left: 40px; width: 120px; text-align: center; top: 113px; font-size: 32px; }
  .label--sauce .product-type { top: 153px; font-size: 15.5px; }
  .label--sauce .ingredients { left: 10px; right: 10px; top: 199px; font-size: 8.5px; }
  .label--sauce .meta-row { left: 12px; right: 14px; top: 252px; }
  .label--sauce .meta-row__note { font-size: 7px; }
  .label--sauce .meta-row__size { font-size: 10px; }
  .label--sauce .address { top: 279px; font-size: 8.5px; }
</style>
</head>
<body>
  <section class="label label--syrup">
    <div class="farm-scene" role="img" aria-label="Faint line sketch of farm fields, barns and village"></div>
    <div class="brand"><span class="brand__dot"></span>FENWICK HOLLOW FARM</div>
    <h1 class="product-name center-line">IRON OATH</h1>
    <p class="product-type center-line">Maple Syrup</p>
    <p class="ingredients">ingredients: Lorem Ipsum, Proin gravida, nibh vel velit, auctor aliquet. Aenean sollicitudin, lorem</p>
    <div class="meta-row">
      <span class="meta-row__note">Refrigerate after opening</span>
      <span class="meta-row__size">16 fl oz</span>
    </div>
    <p class="address center-line">214, Alder Ln, Dunmore ME,04000</p>
  </section>

  <section class="label label--sauce">
    <div class="farm-scene" role="img" aria-label="Faint line sketch of farm fields and hills"></div>
    <div class="brand"><span class="brand__dot"></span>FENWICK HOLLOW FARM</div>
    <div class="korean-art" role="img" aria-label="Crossed wooden chopsticks with a red Korean chili pepper"></div>
    <h2 class="product-name">POMRAK</h2>
    <p class="product-type center-line">Korean HOT SAUCE</p>
    <p class="ingredients">ingredients: Lorem Ipsum, Proin gravida, nibh vel velit, auctor aliquet. Aenean sollicitudin, lorem quis</p>
    <div class="meta-row">
      <span class="meta-row__note">Keep Refrigerated</span>
      <span class="meta-row__size">5.5oz</span>
    </div>
    <p class="address center-line">214, Alder Ln, Dunmore ME,04000</p>
  </section>
</body>
</html>
```